Business card design needed

It's a new business in town.Something so the name stands out.I need a logo for the B.R.K
I may all so use the design as a sign on a building

Contact Information for Business Card

B.R.K
Brackenvale Auto Detailing
42 Tillbury Crs
Brackenvale Vic 3819
Ph:(03)58264027
Mob:0417392658

```html
<!DOCTYPE html>
<html lang="en">
<head>
<meta charset="utf-8">
<title>B.R.K Business Card</title>
<link href="https://fonts.googleapis.com/css2?family=Open+Sans:ital,wght@0,400;0,700;1,400&display=swap" rel="stylesheet">
<style>
  :root {
    --bg-top: #b3b2b3;
    --bg-bottom: #f4f4f4;
    --card: #ffffff;
    --brand-blue: #1a78c2;
    --ink: #231f20;
    --navy: #2b3384;
    --band-dark: #1c1c1c;
    --band-light: #5e5e5e;
    --rule: #9a9a9a;
  }
  * { box-sizing: border-box; margin: 0; padding: 0; }
  html, body { width: 1200px; height: 912px; overflow: hidden; }
  body {
    background: linear-gradient(180deg, var(--bg-top) 0%, #cfcfcf 45%, var(--bg-bottom) 75%, #ffffff 100%);
    font-family: "Open Sans", sans-serif;
    color: var(--ink);
    position: relative;
  }
  .card {
    position: absolute;
    left: 370px;
    width: 460px;
    height: 270px;
    background: var(--card);
    border-radius: 20px;
    box-shadow: 0 10px 24px rgba(0,0,0,0.25);
    overflow: hidden;
  }
  .card--front { top: 140px; }
  .card--back { top: 480px; }

  .brand-name {
    font-weight: 700;
    color: var(--brand-blue);
    letter-spacing: 2px;
    line-height: 1;
  }
  .card--front .brand-name {
    position: absolute;
    left: 0; right: 0; top: 50%;
    transform: translateY(-50%);
    text-align: center;
    font-size: 58px;
  }
  .card--back .brand-name {
    position: absolute;
    left: 26px; top: 24px;
    font-size: 40px;
  }

  .holder {
    position: absolute;
    left: 0; right: 0; top: 122px;
    text-align: center;
  }
  .holder__name { font-weight: 700; font-size: 13px; }
  .holder__role { font-style: italic; font-size: 11px; }

  .contact {
    position: absolute;
    top: 166px; left: 0; right: 0;
    display: flex;
    font-size: 11px;
    line-height: 19px;
  }
  .contact__lines {
    width: 184px;
    flex: none;
    padding-right: 8px;
    text-align: right;
  }
  .contact__line { display: flex; justify-content: flex-end; align-items: center; gap: 4px; white-space: nowrap; }
  .contact__line svg { width: 13px; height: 13px; flex: none; }
  .contact__divider { width: 1px; flex: none; background: var(--rule); height: 58px; }
  .contact__address { padding-left: 8px; padding-right: 20px; white-space: nowrap; }

  .band {
    position: absolute;
    left: 0; right: 0; bottom: 0;
    height: 34px;
  }
</style>
</head>
<body>

  <section class="card card--front" aria-label="Card front">
    <div class="brand-name">B.R.K</div>
  </section>

  <section class="card card--back" aria-label="Card back">
    <div class="brand-name">B.R.K</div>

    <div class="holder">
      <p class="holder__name">Dario Velencourt</p>
      <p class="holder__role">Manager</p>
    </div>

    <div class="contact">
      <div class="contact__lines">
        <p class="contact__line">(03)58264027
          <svg viewBox="0 0 14 14"><rect x="1" y="1" width="12" height="12" rx="3" fill="none" stroke="#231f20" stroke-width="1.2"/><path d="M4.5 4c0 3 2 5.5 5 5.5l.6-1.4-1.5-.8-.7.7c-.9-.4-1.6-1.1-2-2l.7-.7-.8-1.5z" fill="#231f20"/></svg>
        </p>
        <p class="contact__line">0417392658
          <svg viewBox="0 0 14 14"><rect x="4" y="1" width="6" height="12" rx="1.2" fill="none" stroke="#231f20" stroke-width="1.2"/><rect x="5.3" y="2.8" width="3.4" height="4" fill="#231f20"/><circle cx="7" cy="10.6" r=".8" fill="#231f20"/></svg>
        </p>
        <p class="contact__line">www.BRK.com
          <svg viewBox="0 0 14 14"><circle cx="7" cy="7" r="5.8" fill="none" stroke="#231f20" stroke-width="1.2"/><ellipse cx="7" cy="7" rx="2.4" ry="5.8" fill="none" stroke="#231f20" stroke-width="1"/><path d="M1.2 7h11.6M2 4h10M2 10h10" stroke="#231f20" stroke-width="1"/></svg>
        </p>
      </div>
      <div class="contact__divider"></div>
      <div class="contact__address">
        <p>Brackenvale Auto Detailing 42 Tillbury Crs</p>
        <p>Brackenvale Vic 3819</p>
      </div>
    </div>

    <svg class="band" viewBox="0 0 460 34" preserveAspectRatio="none" aria-hidden="true">
      <defs>
        <linearGradient id="band-blue" x1="0" x2="1">
          <stop offset="0" stop-color="#2b3384"/>
          <stop offset="0.6" stop-color="#1a6cc0"/>
          <stop offset="1" stop-color="#2b3384"/>
        </linearGradient>
        <linearGradient id="band-dark" x1="0" x2="1">
          <stop offset="0" stop-color="#1c1c1c"/>
          <stop offset="0.45" stop-color="#5e5e5e"/>
          <stop offset="1" stop-color="#1c1c1c"/>
        </linearGradient>
      </defs>
      <rect x="0" y="24" width="250" height="10" fill="url(#band-blue)"/>
      <path d="M232 34 L250 12 L460 12 L460 34 Z" fill="url(#band-dark)"/>
    </svg>
  </section>

</body>
</html>
```